Mechanical Engineering Business needs a Label Design for Bottle.

We need a Label design for 2 Bottle Sizes of Cutting Paste. This is used for Machine Work Shops big and small to do applications for different cutting processes. Example : Tapping / Broaching / Drilling / Reaming / Knurling / etc. An example of a similar product can be found at https://grivolex.com/product/16-oz-grivolex-bottle/ ... https://grivolex.com/product/2-oz-grivolex-bottle/ ... Our product will be named Mil - Gel or Milling - Gel with our Company logo attached. Currently, we are open to ideas and do not have any fixed concept.

```html
<!DOCTYPE html>
<html lang="en">
<head>
<meta charset="utf-8">
<title>Mil-Gel Machining Lubricant Label</title>
<link rel="stylesheet" href="https://fonts.googleapis.com/css2?family=Archivo:ital,wght@0,300;0,400;0,800;0,900;1,800;1,900&display=swap">
<style>
  :root {
    --backdrop: #e7e7e9;
    --label-black: #050505;
    --label-charcoal: #2b2b2d;
    --band-mauve: #c4b3bd;
    --brand-maroon: #7d1d36;
    --ink-dark: #111111;
    --ink-light: #f4f4f4;
    --ink-soft: #d9d9d9;
  }
  * { margin: 0; padding: 0; box-sizing: border-box; }
  html, body {
    width: 1200px; height: 1034px; overflow: hidden;
    background: var(--backdrop);
    font-family: "Archivo", Arial, sans-serif;
  }
  .label {
    position: absolute; left: 403px; top: 57px;
    width: 394px; height: 920px;
    background: linear-gradient(180deg, var(--label-charcoal) 0%, #141414 22%, var(--label-black) 42%, var(--label-black) 100%);
    box-shadow: 4px 6px 10px rgba(0,0,0,0.28);
    color: var(--ink-light);
    text-align: center;
  }
  .brand {
    position: absolute; left: 0; right: 0; top: 120px;
    display: flex; justify-content: center; align-items: center; gap: 12px;
  }
  .brand-dot {
    width: 26px; height: 26px; border-radius: 50%;
    background: var(--brand-maroon);
  }
  .brand-name {
    font-weight: 400; font-size: 30px; letter-spacing: 0.5px;
    color: var(--ink-soft);
  }
  .product-name {
    position: absolute; left: 0; right: 0; top: 228px;
    font-size: 60px; line-height: 64px; letter-spacing: -1px;
  }
  .product-name .bold { font-weight: 900; }
  .product-name .light { font-weight: 300; }
  .band {
    position: absolute; left: 0; right: 0;
    background: var(--band-mauve);
    color: var(--ink-dark);
    display: flex; align-items: center; justify-content: center;
  }
  .band-category {
    top: 323px; height: 62px;
    clip-path: polygon(0 6%, 55% 0, 100% 3%, 100% 96%, 45% 100%, 0 94%);
    font-style: italic; font-weight: 900; font-size: 26px;
  }
  .grade-tag {
    position: absolute; left: 49px; top: 415px;
    width: 295px; height: 40px;
    border: 1px solid #9a9a9a;
    border-radius: 0 14px 0 14px;
    display: flex; align-items: center; justify-content: center;
    font-style: italic; font-weight: 900; font-size: 21px;
  }
  .formula {
    position: absolute; left: 0; right: 0; top: 484px;
    font-weight: 900; font-size: 38px; line-height: 44px;
    color: var(--band-mauve);
  }
  .applications {
    position: absolute; left: 0; right: 0; top: 600px;
    list-style: none;
    font-weight: 300; font-size: 25px; line-height: 31.5px;
  }
  .band-warning {
    top: 775px; height: 64px;
    clip-path: polygon(0 3%, 50% 0, 100% 5%, 100% 97%, 50% 100%, 0 95%);
    font-weight: 900; font-size: 25px; letter-spacing: 0.5px;
  }
  .net-weight {
    position: absolute; left: 0; right: 0; top: 852px;
    font-weight: 900; font-size: 18px;
  }
</style>
</head>
<body>
  <main class="label">
    <div class="brand">
      <span class="brand-dot"></span>
      <span class="brand-name">HALVERN TOOLS</span>
    </div>
    <h1 class="product-name"><span class="bold">MIL</span><span class="light">-GEL</span></h1>
    <div class="band band-category">MACHINING LUBRICANT</div>
    <div class="grade-tag">Professional Grade</div>
    <p class="formula">THICK<br>FORMULA</p>
    <ul class="applications">
      <li>TAPPING</li>
      <li>BROACHING</li>
      <li>DRILLING</li>
      <li>REAMING</li>
      <li>KNURLING</li>
    </ul>
    <div class="band band-warning">SHAKE WELL</div>
    <p class="net-weight">NET WT.16–OZ</p>
  </main>
</body>
</html>
```